Pelovina: National Baking Mix Company Needs a Pancake And Waffle Mix Label Design

Hi, we are looking for a front label design for a new pancake and waffle mix. We currently develop and manufacture various dry mixes for crepes, pancakes, waffles, and waffle cones. We are looking to expand our product line into the "all natural" category of foods. This new pancake mix contains the highest quality ingredients including: (whole grain brown rice flour, whole grain oat flour, golden flaxseed meal, whole grain sorghum flour, organic coconut flour, organic coconut sugar, eggs, leavening, vanilla extract, salt, spices.) We are looking for a way to communicate these ingredients to the public by means of claims like one would see on a food label. Here are a few different companies that do it well.
https://toskwelder.com/product/paleo/
https://www.brightquern.com/collections/almond-flour-baking-mixes/products/almond-flour-pancake-waffle-mix
https://morwickoven.com/product/paleo-pancake-waffle-mix/
https://pelovina.com
Our mix is a just add water only mix and consists of whole grains, is gluten free, dairy free, soy free, preservative free, contains no artificial ingredients whatsoever, NON-GMO, kosher, low in sodium, good source of fiber and iron, contains omega-3 fatty acids etc. We need a strong and attractive design that appeals to the customer on a grocery store shelf. This mix is a healthier option compared to traditional pancake/waffle mixes but still provides great taste and texture one would expect from a pancake mix. Label design should be around 4.25"x 6.75" tall ways. We want to utilize what we have to offer in the best way possible.

Target Market(s)

All Natural, Healthy, Pancake Mix. 20yr-50yr olds primariliy

Industry/Entity Type

Grocery Store

Font styles to use
Serif
Sans Serif
Decorative

Colors

Designer to choose colors to be used in the design.

Requirements
Must have
• Name of company "Pelovina", must say "Pancake & Waffle Mix", "Just add water", "gluten free", "dairy free", "whole grains". the rest is up to you!
Nice to have
• I would like to see the claims utilized and promoted in such ways that appeal to the consumer. The all natural category of food is growing and we want to take advantage of that food category.
Should not have
• Should not say "paleo" on label. This mix is within the category but cannot be labeled as such.

```html
<!DOCTYPE html>
<html lang="en">
<head>
<meta charset="utf-8">
<title>Pelovina Pancake &amp; Waffle Mix – Front Label</title>
<link href="https://fonts.googleapis.com/css2?family=Bebas+Neue&family=Barlow+Condensed:wght@500;600&family=Oswald:wght@500&family=Kaushan+Script&family=Lora:ital,wght@1,700&family=Roboto:wght@400&display=swap" rel="stylesheet">
<style>
  :root {
    --leaf: #3f9a2c;
    --leaf-light: #a6c93a;
    --paper: #ebe8e2;
    --cream: #efe4b8;
    --orange: #f39a25;
    --brown: #7a4322;
    --ink: #222;
    --white: #fff;
  }
  * { margin: 0; padding: 0; box-sizing: border-box; }
  html, body { width: 764px; height: 1200px; overflow: hidden; background: var(--white); }
  .sheet { position: relative; width: 764px; height: 1200px; font-family: "Roboto", sans-serif; color: var(--ink); }

  .brand-header { position: absolute; left: 0; width: 764px; top: 70px; text-align: center; }
  .brand-header .wordmark { font-family: "Lora", serif; font-style: italic; font-weight: 700; font-size: 76px; color: var(--ink); line-height: 1; }
  .brand-header .tagline { font-family: "Lora", serif; font-style: italic; font-weight: 700; font-size: 22px; color: var(--ink); margin-top: 30px; }

  .dims { position: absolute; inset: 0; }
  .dim-label { position: absolute; font-family: "Roboto", sans-serif; font-size: 19px; color: var(--ink); }
  .dim-width { left: 370px; top: 256px; }
  .dim-flap { left: 697px; top: 366px; }
  .dim-height { left: 68px; top: 690px; transform: rotate(-90deg); }

  .label { position: absolute; left: 123px; top: 303px; width: 532px; height: 799px; background: var(--paper); overflow: hidden; }
  .label-bg { position: absolute; inset: 0; }

  .claim-ribbon { position: absolute; left: 392px; top: 0; width: 76px; height: 346px; }
  .ribbon-claim { position: absolute; left: 0; width: 76px; text-align: center; font-family: "Barlow Condensed", sans-serif; font-weight: 500; font-size: 14px; color: var(--white); line-height: 1; }
  .ribbon-icon { position: absolute; left: 16px; width: 43px; height: 43px; }

  .label-brand { position: absolute; left: 66px; top: 150px; width: 220px; text-align: center; }
  .label-brand .wordmark { font-family: "Lora", serif; font-style: italic; font-weight: 700; font-size: 34px; color: var(--ink); line-height: 1; }
  .label-brand .tagline { font-family: "Lora", serif; font-style: italic; font-weight: 700; font-size: 10px; margin-top: 12px; color: var(--ink); }

  .product-name { position: absolute; left: 68px; top: 238px; font-family: "Bebas Neue", sans-serif; font-weight: 400; color: var(--brown); line-height: 0.8; font-size: 104px; letter-spacing: 0; }
  .product-mix { position: absolute; left: 350px; top: 330px; font-family: "Kaushan Script", cursive; color: var(--orange); font-size: 66px; line-height: 1; transform: rotate(-6deg); }

  .water-banner { position: absolute; left: 0; top: 432px; width: 310px; height: 80px; }
  .water-text { position: absolute; left: 90px; top: 452px; font-family: "Oswald", sans-serif; font-weight: 500; font-size: 30px; line-height: 1.2; color: var(--white); transform: rotate(-7deg); transform-origin: left center; }

  .side-claims { position: absolute; left: 68px; top: 520px; width: 130px; }
  .side-claim { text-align: center; margin-bottom: 8px; }
  .side-claim svg { display: block; margin: 0 auto; width: 38px; height: 38px; }
  .side-claim span { display: block; font-family: "Barlow Condensed", sans-serif; font-weight: 600; font-size: 13px; color: var(--leaf); margin-top: 2px; }

  .serving-photo { position: absolute; left: 160px; top: 480px; width: 330px; height: 255px; border-radius: 45% 45% 35% 35%; background: radial-gradient(ellipse at 60% 50%, #e9b56b 0%, #d9964c 45%, rgba(217,150,76,0.35) 68%, rgba(235,232,226,0) 80%); }

  .net-band { position: absolute; left: 0; bottom: 0; width: 532px; height: 50px; background: var(--brown); }
  .net-weight { position: absolute; right: 58px; top: 10px; font-family: "Barlow Condensed", sans-serif; font-weight: 500; font-size: 21px; color: var(--white); }
</style>
</head>
<body>
<div class="sheet">

  <header class="brand-header">
    <div class="wordmark">Pelovina</div>
    <div class="tagline">Simply real, honestly wholesome food!</div>
  </header>

  <svg class="dims" width="764" height="1200" viewBox="0 0 764 1200">
    <g stroke="#222" stroke-width="1" fill="none">
      <line x1="123" y1="283" x2="655" y2="283"/>
      <line x1="123" y1="273" x2="123" y2="293"/>
      <line x1="655" y1="273" x2="655" y2="293"/>
      <path d="M131 279 L123 283 L131 287 M647 279 L655 283 L647 287"/>
      <line x1="98" y1="303" x2="98" y2="1102"/>
      <line x1="88" y1="303" x2="108" y2="303"/>
      <line x1="88" y1="1102" x2="108" y2="1102"/>
      <path d="M94 311 L98 303 L102 311 M94 1094 L98 1102 L102 1094"/>
      <line x1="689" y1="303" x2="689" y2="436"/>
      <line x1="679" y1="303" x2="699" y2="303"/>
      <line x1="679" y1="436" x2="699" y2="436"/>
      <path d="M685 311 L689 303 L693 311 M685 428 L689 436 L693 428"/>
      <line x1="130" y1="436" x2="665" y2="436" stroke-dasharray="4 3"/>
    </g>
  </svg>
  <div class="dim-label dim-width">6 in.</div>
  <div class="dim-label dim-flap">1.5 in.</div>
  <div class="dim-label dim-height">9 in.</div>

  <section class="label">
    <svg class="label-bg" width="532" height="799" viewBox="0 0 532 799">
      <defs>
        <linearGradient id="leafGradient" x1="0" y1="0" x2="1" y2="1">
          <stop offset="0" stop-color="#3f9a2c"/>
          <stop offset="0.6" stop-color="#6fae32"/>
          <stop offset="1" stop-color="#b3cf3c"/>
        </linearGradient>
      </defs>
      <path d="M0 0 H532 V290 C470 200 330 150 220 190 C130 225 60 290 0 340 Z" fill="url(#leafGradient)"/>
      <path d="M0 360 C90 250 230 90 430 80" stroke="#efe4b8" stroke-width="14" fill="none" opacity="0.85"/>
      <path d="M0 300 C120 200 280 130 470 120" stroke="#c9dc6a" stroke-width="6" fill="none" opacity="0.7"/>
    </svg>

    <div class="claim-ribbon">
      <svg width="76" height="346" viewBox="0 0 76 346">
        <path d="M0 0 H76 V346 L38 330 L0 346 Z" fill="var(--orange)"/>
      </svg>
      <svg class="ribbon-icon" style="top:160px" viewBox="0 0 44 44" fill="none" stroke="#fff" stroke-width="2.5">
        <circle cx="22" cy="22" r="19"/><path d="M22 12 V34 M22 18 l-5 -4 M22 18 l5 -4 M22 25 l-5 -4 M22 25 l5 -4"/><line x1="9" y1="9" x2="35" y2="35"/>
      </svg>
      <div class="ribbon-claim" style="top:209px">Gluten-free</div>
      <svg class="ribbon-icon" style="top:232px" viewBox="0 0 44 44" fill="none" stroke="#fff" stroke-width="2.5">
        <circle cx="22" cy="22" r="19"/><path d="M18 11 H26 V16 L29 21 V33 H15 V21 L18 16 Z" fill="#fff"/><line x1="9" y1="9" x2="35" y2="35"/>
      </svg>
      <div class="ribbon-claim" style="top:281px">Dairy-free</div>
      <svg class="ribbon-icon" style="top:290px; display:none" viewBox="0 0 44 44"></svg>
      <div class="ribbon-claim" style="top:312px">Nut Free</div>
    </div>

    <div class="label-brand">
      <div class="wordmark">Pelovina</div>
      <div class="tagline">Simply real, honestly wholesome food!</div>
    </div>

    <h1 class="product-name">PANCAKE<br>&amp; WAFFLE</h1>
    <div class="product-mix">Mix</div>

    <svg class="water-banner" viewBox="0 0 310 80">
      <path d="M0 40 L303 0 L310 50 L0 80 Z" fill="var(--orange)"/>
    </svg>
    <div class="water-text">Just add water!</div>

    <div class="side-claims">
      <div class="side-claim">
        <svg viewBox="0 0 38 38"><circle cx="19" cy="19" r="19" fill="var(--leaf)"/><path d="M13 24 L22 11 L27 15 L18 28 Z" fill="#fff"/><line x1="8" y1="8" x2="30" y2="30" stroke="#fff" stroke-width="2"/></svg>
        <span>Low Sodium</span>
      </div>
      <div class="side-claim">
        <svg viewBox="0 0 38 38"><circle cx="19" cy="19" r="19" fill="var(--leaf)"/><path d="M15 12 H23 M17 12 V19 L12 28 H26 L21 19 V12" fill="#fff" stroke="#fff" stroke-width="1.5"/><line x1="8" y1="8" x2="30" y2="30" stroke="#fff" stroke-width="2"/></svg>
        <span>Non GMO</span>
      </div>
      <div class="side-claim">
        <svg viewBox="0 0 38 38"><circle cx="19" cy="19" r="19" fill="var(--leaf)"/><path d="M14 26 L23 13 L27 16 L18 29 Z" fill="#fff"/><line x1="8" y1="8" x2="30" y2="30" stroke="#fff" stroke-width="2"/></svg>
        <span>Preservative Free</span>
      </div>
      <div class="side-claim">
        <svg viewBox="0 0 38 38"><circle cx="19" cy="19" r="19" fill="var(--leaf)"/>
          <text x="19" y="12" text-anchor="middle" font-family="Barlow Condensed, sans-serif" font-size="5" fill="#fff">MADE WITH</text>
          <text x="19" y="18" text-anchor="middle" font-family="Barlow Condensed, sans-serif" font-size="5" fill="#fff">GLUTEN FREE</text>
          <text x="19" y="24" text-anchor="middle" font-family="Barlow Condensed, sans-serif" font-size="5" fill="#fff">WHOLE</text>
          <text x="19" y="30" text-anchor="middle" font-family="Barlow Condensed, sans-serif" font-size="5" fill="#fff">GRAINS</text>
        </svg>
      </div>
    </div>

    <div class="serving-photo" role="img" aria-label="Stack of golden pancakes with syrup, raspberries, mint and scattered blueberries"></div>

    <div class="net-band"><div class="net-weight">NET WT: 16 oz. (454g)</div></div>
  </section>

</div>
</body>
</html>
```